Biz technology consulting firm like a global company (better than Corvellant, etc)

Check word document high level requirements, a_design_webpage_content attached providing more details for content and message to convey to potential customers..  Create a crisp, clear and engaging business consulting website design that allows the user to understand the value that Brimquora can deliver to their company.  We focus on innovation, simplification, creative solutions, digital transformations ERP, CRM, Analytics, project management, making IT simple and coaching enterprises how to align and implement technologies to support business strategy and goals. Whether a startup or a global billion dollar firm, we increase EBITDA through innovation and digital transformation.  

I desire to have sections that highlight each of the core areas such as: (**Please see  brimquora.example and the design word document that is attached below for core areas of focus**)

Feel free to go to Brimquora.example and review the basic categories to understand at a very high level the categories that are key.

Help me create a brand and website that engages startups, Private Equity firms seeking carve-out, integration experience and large corporate enterprises searching to convert to data driven and customer focused enterprises.  
Hero section with a tagline that emphasizes the company's focus on Tilting the view.  We help you visualize outcomes with a positive and collaborative solution driven mindset.  When you look at life through a different "positive" lens, you can convert all problems to opportunities.  Align your IT team with your business goals and you quickly realize the value of all processes and technology deployed in your enterprise; increasing EBITDA, morale, and long term success.

We evaluate your current state, create a custom roadmap for alignment, coach  and empower you to lead while removing the uncertainty and silos.  Partner with the experts who help make business and technology simple and effective
Call-to-action section encouraging visitors to learn more about the company's services and expertise
Services -- detail provided in the attached word document (please use)
Section providing an overview of the company's services, including digital transformation, strategy, change management, CRM, ERP, automation, AI, data / analytics, process optimization, carve-outs, integrations, scaling, risk mitigation, security and marketing.
Call-to-action section encouraging visitors to learn more about the company's expertise and how it can help their business and encouraging visitors to schedule a consultation or assessment.
Footer
Navigation menu
Contact information
LinkedIn link
The website should have a modern and professional design, with a focus on clear messaging and easy navigation. The color scheme will be clean and simple, with a mix of colors to convey trust, reliability, and innovation. The website will be optimized for search engines and mobile devices, ensuring that visitors can easily access the site from any device.

Companies who desire to grow their business, optimize their processes, maximize the output of human capital and profitablity.

Business Technology consulting

• designer should choose for professional audience

• easy navigation, engaging flow, professional layout and colors that represent confidence, excellence and innovation in a world full of change.
• I would like to see you blend in the play on PIVOT's (changes that we face in business and life), the different way we may look at things and the unique way we solve problems. All of these are options to Tilt the view and leverage the unique views of individuals, millions of data points, workflow and technology enablers to deliver maximize value to your enterprise

```html
<!DOCTYPE html>
<html lang="en">
<head>
<meta charset="utf-8">
<title>brimquora — Change Simply Happens</title>
<link href="https://fonts.googleapis.com/css2?family=Roboto:wght@400;500;700;900&display=swap" rel="stylesheet">
<style>
  :root {
    --navy: #2f3a80;
    --navy-deep: #1f2a63;
    --lavender: #eef0fb;
    --lavender-band: #e8eaf8;
    --ink: #3b3b3b;
    --muted: #6c7090;
    --white: #ffffff;
    --black: #000000;
    --link: #4a5aa8;
  }
  * { box-sizing: border-box; margin: 0; padding: 0; }
  html, body { width: 1200px; height: 3857px; overflow: hidden; background: var(--white); }
  body { position: relative; font-family: "Roboto", sans-serif; color: var(--ink); }

  .hero-backdrop { position: absolute; left: 0; top: 0; width: 1200px; height: 880px; }
  .nav { position: absolute; top: 50px; left: 0; width: 1200px; height: 20px; }
  .nav-link { position: absolute; top: 2px; font-size: 11px; color: var(--link); text-decoration: none; }
  .brand { position: absolute; left: 0; width: 1220px; top: -4px; text-align: center; font-size: 21px; font-weight: 700; color: var(--navy); }
  .nav-button { position: absolute; left: 929px; top: -2px; width: 133px; height: 21px; background: var(--navy-deep); color: var(--white); font-size: 8px; font-weight: 500; display: flex; align-items: center; justify-content: center; letter-spacing: .3px; }

  .hero-title { position: absolute; left: 136px; top: 262px; font-size: 82px; line-height: 84px; font-weight: 900; color: var(--navy); letter-spacing: -.5px; }
  .hero-art { position: absolute; left: 665px; top: 150px; width: 535px; height: 660px; border-radius: 40px 0 0 60px; background: linear-gradient(160deg, #d5d9f1 0%, #a9b0dd 55%, #5a64a8 100%); opacity: .85; }

  .intro { position: absolute; left: 150px; width: 900px; text-align: center; }
  .intro h2 { font-size: 33px; font-weight: 700; color: var(--navy); letter-spacing: -.2px; }
  .intro p { margin-top: 10px; font-size: 23.5px; line-height: 29.5px; color: var(--ink); padding: 0 32px; }

  .section-title { position: absolute; left: 0; width: 1200px; text-align: center; font-size: 33px; font-weight: 700; color: var(--navy); }

  .service { position: absolute; width: 420px; text-align: center; }
  .service-art { margin: 0 auto; border-radius: 28px; }
  .service-caption { position: absolute; left: 0; width: 420px; font-size: 20px; line-height: 29.5px; font-weight: 700; color: var(--navy); }

  .focus { position: absolute; left: 0; top: 2956px; width: 1200px; height: 624px; background: var(--black); color: var(--white); }
  .focus h2 { position: absolute; left: 0; width: 1200px; text-align: center; font-size: 33px; font-weight: 700; }
  .focus .tagline { position: absolute; left: 0; top: 114px; width: 1200px; text-align: center; font-size: 23px; }
  .focus-list { position: absolute; top: 254px; list-style: none; }
  .focus-list li { position: relative; padding-left: 22px; font-size: 24px; line-height: 29.5px; margin-bottom: 15.5px; }
  .focus-list li::before { content: ""; position: absolute; left: 0; top: 13px; width: 5px; height: 5px; border-radius: 50%; background: var(--white); }

  .closing-title { position: absolute; left: 0; top: 3609px; width: 1200px; text-align: center; font-size: 33px; font-weight: 700; color: #111; }

  .footer { position: absolute; left: 0; top: 3673px; width: 1200px; height: 184px; background: var(--lavender-band); }
  .footer-statement { position: absolute; left: 110px; top: 27px; width: 980px; text-align: center; font-size: 21.5px; line-height: 29px; font-weight: 700; color: var(--muted); }
  .footer-rule { position: absolute; left: 138px; top: 117px; width: 924px; height: 1px; background: #cfd2e6; }
  .footer-link { position: absolute; top: 137px; font-size: 10.5px; color: #8d90aa; text-decoration: none; }
  .social { position: absolute; top: 138px; width: 10px; height: 10px; border-radius: 50%; border: 1.5px solid #a3a7c2; }
</style>
</head>
<body>

  <svg class="hero-backdrop" viewBox="0 0 1200 880" aria-hidden="true">
    <path d="M576 0 C520 80 470 180 420 300 C340 500 360 760 520 845 C560 868 620 874 700 874 L1200 876 L1200 0 Z" fill="var(--lavender)"/>
  </svg>

  <header class="nav">
    <a class="nav-link" style="left:138px" href="#">Home</a>
    <a class="nav-link" style="left:218px" href="#">About</a>
    <a class="nav-link" style="left:299px" href="#">Contact</a>
    <div class="brand">brimquora</div>
    <div class="nav-button">SERVICES</div>
  </header>

  <h1 class="hero-title">Change<br>Simply<br>Happens</h1>
  <div class="hero-art" role="img" aria-label="Illustration of a consultant arranging interface elements on a large monitor, with colour swatches and gears"></div>

  <section class="intro" style="top:1000px">
    <h2>TRANSFORMING THE WAY YOU DO BUSINESS</h2>
    <p>Every business is unique. That's why we take a personalized approach to every project, working closely with you to understand your goals and create tailored solutions that work for you.</p>
  </section>

  <section class="intro" style="top:1273px">
    <h2>INNOVATIVE SOLUTIONS</h2>
    <p>We believe in pushing the boundaries of what is possible. Our team of experts are dedicated to crafting innovative solutions that help your business thrive. From cutting-edge AI and analytics to customer loyalty and digital transformation, we provide what you need to succeed in today's fast-paced business world.</p>
  </section>

  <h2 class="section-title" style="top:1591px">SERVICES</h2>

  <div class="service" style="left:122px;top:1679px">
    <div class="service-art" role="img" aria-label="Illustration of a dashboard with a target and analytics charts" style="width:330px;height:218px;background:linear-gradient(135deg,#dfe3fb,#f08a7a 55%,#4a55d6)"></div>
    <p class="service-caption" style="top:251px">SaaS CRM (Loyalty &amp; Subscription)<br>Apps / Segmentation / Rewards</p>
  </div>
  <div class="service" style="left:664px;top:1679px">
    <div class="service-art" role="img" aria-label="Illustration of a strategy dashboard with a target and charts" style="width:330px;height:218px;background:linear-gradient(135deg,#dfe3fb,#f08a7a 55%,#4a55d6)"></div>
    <p class="service-caption" style="top:251px">Strategy / Org Design / Competitive<br>Analysis / Change Management</p>
  </div>

  <div class="service" style="left:122px;top:2091px">
    <div class="service-art" role="img" aria-label="Illustration of a team in a training session" style="width:300px;height:243px;background:linear-gradient(150deg,#eef1fb,#9fb4ea 55%,#1f4fc4)"></div>
    <p class="service-caption" style="top:268px">M&amp;A - (Carve-outs / Integrations)<br>Diligence / TSA / IMO / Interim CxO</p>
  </div>
  <div class="service" style="left:664px;top:2091px">
    <div class="service-art" role="img" aria-label="Illustration of two people presenting a growth chart on a digital transformation dashboard" style="width:446px;height:243px;background:linear-gradient(150deg,#eef1fb,#b9c4f3 55%,#7f8ee6)"></div>
    <p class="service-caption" style="top:268px">Digital Transformation, App Dev,<br>Social/Omni-channel solutions</p>
  </div>

  <div class="service" style="left:122px;top:2525px">
    <div class="service-art" role="img" aria-label="Illustration of a person operating process gears with a progress bar" style="width:240px;height:235px;background:linear-gradient(150deg,#f2f4fb,#b7c6ef 55%,#2c67d8)"></div>
    <p class="service-caption" style="top:272px">Process Optimization - Secure,<br>Scalable, Compliant Systems</p>
  </div>
  <div class="service" style="left:664px;top:2525px">
    <div class="service-art" role="img" aria-label="Illustration of a team analysing data on a large monitor" style="width:350px;height:235px;background:linear-gradient(150deg,#e7eefb,#a8c1ee 55%,#2e4a9a)"></div>
    <p class="service-caption" style="top:264px">AI / Analytics / Automation</p>
  </div>

  <section class="focus">
    <h2 style="top:66px">THINK - CREAT - SOLVE</h2>
    <p class="tagline">Helping businesses of all sizes reach their full potential.</p>
    <h2 style="top:176px">AREAS OF FOCUS:</h2>
    <ul class="focus-list" style="left:98px;width:470px">
      <li>Strategy / Value Creation / Interim CxO</li>
      <li>CRM and loyalty solutions - Customer engagement</li>
      <li>M&amp;A (Integration / Carve-outs / IMO / TSAs</li>
      <li>Change management / Org Design</li>
      <li>Digital transformation / Application Development</li>
    </ul>
    <ul class="focus-list" style="left:688px;width:450px">
      <li>AI / Analytics / Security</li>
      <li>Customer experience</li>
      <li>Operational/Process optimization, scaling</li>
      <li>Complex global ERP / Compliance</li>
      <li>Shared service / PMO / Automation</li>
    </ul>
  </section>

  <h2 class="closing-title">Unlock potential of vision</h2>

  <footer class="footer">
    <p class="footer-statement">Our team of experts consists of professionals with extensive transformation experience spanning a variety of industries. We are committed to help our clients achieve their goals.</p>
    <div class="footer-rule"></div>
    <a class="footer-link" style="left:138px" href="#">Home</a>
    <a class="footer-link" style="left:218px" href="#">About</a>
    <a class="footer-link" style="left:299px" href="#">Contact</a>
    <span class="social" style="left:897px" aria-label="Social link"></span>
    <span class="social" style="left:935px" aria-label="Social link"></span>
    <span class="social" style="left:973px" aria-label="Social link"></span>
    <span class="social" style="left:1012px" aria-label="Social link"></span>
    <span class="social" style="left:1051px" aria-label="Social link"></span>
  </footer>

</body>
</html>
```